Clinician Harbor Collective

I am a financial planner whose client's are physicians and dentists. As physicians, there is very little time for them to do research on numerous aspects of their business and personal lives. I am looking to build a website that is a 1 stop shop for many of the services/resources they may need. It will be my job to screen the resources/advertisers and place competent people/business's that I know and have a track record on. there will ultimately be 10 or 12 ish areas that I would like to provide resources in:
disability insurance
life insurance
retirement planning
student loan advisors
employment contract and business formation attorneys
accountants
real estate agents
physician mortgages
personal loans
malpractice insurance
physician recruiters
maybe 2 other areas which I have yet to figure out.....
I would like each of these options to be able to be clicked on and a page will open up with the 1 or 2 or 3 or 4 people/business's that I have picked to represent these areas. I would like each specific person/business to have a click here to contact me link in which an email goes to the person and I am copied on the initial correspondence between the physician and the mortgage broker.... just so I can see some of the correspondence they will be receiving.
nowhere on the site do I want it to say my name. there will be certain disclosures that are needed and other wording but I think this is a good starting point.
here are links to two websites with the same general concept. please keep in mind that I want my website to be more on the simple side.
http://www.vantorelmedlink.example/index.html
http://bluestethwealth.example/
Industry/Entity Type
Financial

```html
<!DOCTYPE html>
<html lang="en">
<head>
<meta charset="utf-8">
<title>Clinician Harbor Collective</title>
<link rel="stylesheet" href="https://fonts.googleapis.com/css2?family=Raleway:wght@500;600;700&family=Open+Sans:wght@400;600;700&family=Ubuntu:wght@400;500;700&display=swap">
<style>
:root{
  --blue:#1a4791;
  --blue-deep:#0f3d84;
  --blue-title:#1f4f98;
  --green:#3c9f2f;
  --green-bright:#46ad37;
  --ink:#333;
  --line:#d8d8d8;
  --card:#f3f3f3;
}
*{margin:0;padding:0;box-sizing:border-box}
html,body{width:1029px;height:1200px;overflow:hidden;background:#fff}
body{position:relative;font-family:"Open Sans",Arial,sans-serif;color:var(--ink)}
.abs{position:absolute}

/* header */
.brand{left:88px;top:18px;display:flex;align-items:center;gap:10px}
.brand-dot{width:40px;height:40px;border-radius:50%;background:var(--green)}
.brand-name{font-family:"Raleway",sans-serif;font-weight:700;font-size:24px;color:var(--blue-title);line-height:1.1;width:200px}
.phone{right:89px;top:14px;display:flex;align-items:center;gap:8px;font-family:"Ubuntu",sans-serif;font-weight:500;font-size:19px;color:#444;letter-spacing:.5px}
.phone-ico{width:21px;height:21px;border-radius:3px;background:var(--green);display:flex;align-items:center;justify-content:center}
.follow{right:89px;top:53px;display:flex;align-items:center;gap:9px;font-family:"Ubuntu",sans-serif;font-size:15px;color:#444}
.soc{width:26px;height:26px;border-radius:50%}
.soc.a{background:#2c55b5}.soc.b{background:#c6202a}.soc.c{background:#5aaed6}.soc.d{background:#2f7fb4}.soc.e{background:#f08a1c}

/* nav */
.nav{left:0;top:99px;width:1029px;height:35px;background:var(--blue)}
.nav ul{list-style:none;display:flex;height:100%;align-items:center;padding-left:113px;font-family:"Ubuntu",sans-serif;font-weight:500;font-size:13px;color:#fff}
.nav li{margin-right:29px}
.nav li.current{position:relative}
.nav li.current::before{content:"";position:absolute;left:-12px;top:-14px;width:66px;height:2px;background:var(--green-bright)}

/* hero */
.hero{left:0;top:134px;width:1029px;height:342px;background:linear-gradient(90deg,#2f73b3 0%,#bcd6ea 14%,#eef3f6 36%,#f3ece4 60%,#e7dccf 100%)}
.hero-photo{left:86px;top:38px;width:500px;height:304px;border-radius:4px;background:linear-gradient(180deg,#dfe8f0,#9cc2e3 60%,#7daedc)}
.hero-arrow{top:140px;width:36px;height:36px;border-radius:50%;border:3px solid #b8b8b8;background:rgba(255,255,255,.6);display:flex;align-items:center;justify-content:center}
.hero-title{left:608px;top:110px;font-family:"Raleway",sans-serif;font-weight:600;font-size:32px;color:#111}
.hero-text{left:608px;top:158px;width:330px;font-family:Arial,sans-serif;font-size:13px;line-height:19px;color:#333}
.hero-btn{left:606px;top:218px;width:146px;height:36px;border-radius:18px;background:linear-gradient(#4fb83e,#2f8f24);color:#fff;font-family:"Raleway",sans-serif;font-size:18px;font-weight:500;display:flex;align-items:center;justify-content:center}
.hero-shadow{left:90px;top:476px;width:850px;height:20px;background:radial-gradient(ellipse at top,rgba(0,0,0,.18),transparent 70%)}

/* cards */
.card{top:521px;width:199px;height:140px;border:1px solid var(--line);border-radius:6px;background:linear-gradient(#fff,var(--card));padding:18px 12px 0 18px}
.card h3{font-family:"Raleway",sans-serif;font-weight:500;font-size:16.5px;line-height:20px;color:var(--blue-title);white-space:nowrap;margin-left:12px}
.card p{font-family:"Ubuntu",sans-serif;font-size:11px;line-height:15.5px;color:#333;margin-top:12px}
.card .more{position:absolute;right:14px;bottom:10px;font-family:Arial,sans-serif;font-weight:700;font-size:9.5px;color:var(--blue)}

/* sidebar */
.side{left:95px;top:684px;width:182px;height:277px;border:1px solid var(--line);border-radius:8px;background:linear-gradient(#fff,#eee)}
.side ul{list-style:none;position:absolute;left:0;top:27px;width:100%}
.side li{height:31px;margin:0 14px 0 6px;border-bottom:1px dotted #aaa;display:flex;align-items:center;font-family:Arial,sans-serif;font-size:12px;color:#222;gap:9px}
.side li b{font-size:9px}
.side-active{left:88px;top:711px;width:168px;height:25px;background:var(--blue);clip-path:polygon(0 0,92% 0,100% 50%,92% 100%,0 100%);color:#fff;display:flex;align-items:center;gap:9px;padding-left:13px;font-family:Arial,sans-serif;font-size:12px}
.side-active b{font-size:9px}
.side .more{position:absolute;right:12px;bottom:10px;font-family:Arial,sans-serif;font-weight:700;font-size:11px;color:#333}

/* main copy */
.main{left:311px;top:700px;width:600px}
.main h2{font-family:"Raleway",sans-serif;font-weight:500;font-size:21px;color:var(--blue-title)}
.lead{margin-top:14px;font-size:10px;font-weight:700;line-height:17px;color:#222}
.sub{margin-top:9px;font-size:11px;font-weight:700;color:#66b04a}
.body-copy{margin-top:7px;font-size:11.5px;line-height:19px;color:#222}
.cta{margin-top:23px;font-size:11.5px;font-weight:700;color:#333}

/* footer */
.foot-nav{left:0;top:990px;width:1029px;height:37px;background:var(--green)}
.foot-nav ul{list-style:none;display:flex;align-items:center;height:100%;padding-left:117px;font-family:"Ubuntu",sans-serif;font-size:11.5px;color:#fff}
.foot-nav li::after{content:"|";margin:0 23px 0 26px}
.foot-nav li:last-child::after{content:""}
.footer{left:0;top:1027px;width:1029px;height:173px;background:var(--blue-deep)}
.foot-brand{left:95px;top:1064px;display:flex;align-items:center;gap:10px}
.foot-brand .brand-dot{background:#8aa2c8}
.foot-brand .brand-name{color:#aabbd6;font-size:25px;width:220px}
.copy{left:107px;top:1154px;font-family:Arial,sans-serif;font-size:10.5px;line-height:17px;color:#fff}
.bubble{left:404px;top:1038px}
.bubble-text{left:423px;top:1048px;width:230px;color:#fff}
.bubble-text h4{font-family:"Ubuntu",sans-serif;font-weight:700;font-size:17px}
.bubble-text p{margin-top:6px;font-family:"Ubuntu",sans-serif;font-size:9px;line-height:15.5px;text-align:justify}
.quote-by{left:451px;top:1180px;font-family:Arial,sans-serif;font-size:9.5px;color:#fff}
.touch{left:739px;top:1046px;color:#fff;font-family:Arial,sans-serif}
.touch h4{font-family:"Ubuntu",sans-serif;font-weight:700;font-size:17px}
.touch p{font-size:10px;line-height:14px;margin-top:2px}
.foot-soc{left:741px;top:1124px;display:flex;gap:14px}
.foot-soc .soc{width:27px;height:27px}
.legal{left:744px;top:1173px;font-family:Arial,sans-serif;font-weight:700;font-size:10.5px;color:#fff}
</style>
</head>
<body>

<header>
  <div class="abs brand"><span class="brand-dot"></span><span class="brand-name">Clinician Harbor Collective</span></div>
  <div class="abs phone"><span class="phone-ico"><svg width="12" height="14" viewBox="0 0 12 14"><path d="M2 1h3l1 3-2 1.5c.8 2 2 3.2 3.5 4L9 8l3 1v3c-1 1-2 1-3 1C4 12 0 7 0 3c0-1 1-2 2-2z" fill="#fff"/></svg></span>(555) 014 2290</div>
  <div class="abs follow">Follow Us On <span class="soc a"></span><span class="soc b"></span><span class="soc c"></span></div>
</header>

<nav class="abs nav">
  <ul>
    <li class="current">Home</li><li style="margin-left:25px">About Us</li><li>Archives</li><li style="margin-left:13px">Investing</li><li style="margin-left:4px">Personal Finance</li><li style="margin-left:8px">Retirement</li><li>Advertise Here</li><li style="margin-left:8px">Contact Us</li>
  </ul>
</nav>

<section class="abs hero">
  <div class="abs hero-photo" role="img" aria-label="Group of four smiling physicians in white coats and scrubs with stethoscopes"></div>
  <div class="abs hero-arrow" style="left:43px"><svg width="12" height="14"><path d="M11 1L2 7l9 6z" fill="#aaa"/></svg></div>
  <div class="abs hero-arrow" style="left:948px;top:148px"><svg width="12" height="14"><path d="M1 1l9 6-9 6z" fill="#aaa"/></svg></div>
  <h1 class="abs hero-title">Physician Mortgages</h1>
  <p class="abs hero-text">Lorem Ipsum is simply dummy text of the printing and typesetting industry.</p>
  <div class="abs hero-btn">more details</div>
</section>
<div class="abs hero-shadow"></div>

<section>
  <article class="abs card" style="left:87px"><h3>Disability Insurance</h3><p>Lorem Ipsum is simply dummy text of the printing and typeset-ting industry. Lorem Ipsum has been the industry's...</p><span class="more">More Info [+]</span></article>
  <article class="abs card" style="left:306px"><h3>Life Insurance</h3><p>Lorem Ipsum is simply dummy text of the printing and typeset-ting industry. Lorem Ipsum has been the industry's...</p><span class="more">More Info [+]</span></article>
  <article class="abs card" style="left:524px"><h3>Student Loan</h3><p>Lorem Ipsum is simply dummy text of the printing and typeset-ting industry. Lorem Ipsum has been the industry's...</p><span class="more">More Info [+]</span></article>
  <article class="abs card" style="left:743px"><h3>Personal loans</h3><p>Lorem Ipsum is simply dummy text of the printing and typeset-ting industry. Lorem Ipsum has been the industry's...</p><span class="more">More Info [+]</span></article>
</section>

<aside class="abs side">
  <ul>
    <li></li>
    <li><b>[+]</b>Life insurance</li>
    <li><b>[+]</b>Retirement planning</li>
    <li><b>[+]</b>Student loan advisors</li>
    <li><b>[+]</b>Disability insurance</li>
    <li><b>[+]</b>Life insurance</li>
    <li><b>[+]</b>Retirement planning</li>
  </ul>
  <span class="more">More Info [+]</span>
</aside>
<div class="abs side-active"><b>[+]</b>Disability insurance</div>

<main class="abs main">
  <h2>Employment contract and business formation attorneys</h2>
  <p class="lead">simply dummy text of the printing and typesetting industry. Lorem Ipsum has been the industry's standard dummy text ever since the 1500s, when an unknown printer took a galley of type and scrambled it to make a type specimen book. It has survived not only five centuries,</p>
  <p class="sub">Businesses who have partnered with CHC:</p>
  <p class="body-copy">but also the leap into electronic typesetting, remaining essentially unchanged. It was popularised in the 1960s with the release of Lettrix sheets containing Lorem Ipsum passages, and more recently with desktop publishing software like Pagewell Composer including versions of Lorem Ipsum.</p>
  <p class="cta">What are you waiting for? Call us NOW on 02 5550 1873. We will exceed your expectations.</p>
</main>

<nav class="abs foot-nav">
  <ul><li>Home</li><li>About Us</li><li>Archives</li><li>Investing</li><li>Personal Finance</li><li>Retirement</li><li>Advertise Here</li><li>Contact Us</li></ul>
</nav>

<footer class="abs footer"></footer>
<div class="abs foot-brand"><span class="brand-dot"></span><span class="brand-name">Clinician Harbor Collective</span></div>
<p class="abs copy">Copyright © 2014 Clinician Harbor Collective<br>Disclaimer &nbsp;|&nbsp; All Right Reserved</p>

<svg class="abs bubble" width="266" height="150" viewBox="0 0 266 150">
  <path d="M16 2h234a14 14 0 0 1 14 14v102a14 14 0 0 1-14 14h-44l4 16-22-16H16A14 14 0 0 1 2 118V16A14 14 0 0 1 16 2z" fill="#3ea52f" stroke="#fff" stroke-width="1.5"/>
</svg>
<div class="abs bubble-text">
  <h4>Testimonial</h4>
  <p>Lorem Ipsum is simply dummy text of the printing and typesetting industry. Lorem Ipsum has been the industry's standard dummy text ever since the 1500s, when an unknown printer took a galley of type and scrambled</p>
</div>
<p class="abs quote-by">Marcus Delvane, Pine Hollow, VT</p>

<div class="abs touch">
  <h4>Get in touch</h4>
  <p>Clinician Harbor Collective<br>4720 Orchard Row (at Elm Pkwy) Ste 210,<br>Fairbrook , TX 70000</p>
</div>
<div class="abs foot-soc"><span class="soc b"></span><span class="soc d"></span><span class="soc e"></span><span class="soc c"></span><span class="soc a"></span></div>
<p class="abs legal">Terms &amp; Conditions &nbsp; | &nbsp; Privacy Policy</p>

</body>
</html>
```